Veterinary Pylon

My veterinary clinic is not clearly visible from the street and I want to place a Pylon next to my driveway. I want a modern, elegant straight Design, the Photo shows the sheduled place. One can see the clinic on our Homepage: www.fernhollow-tierpraxis.at
The last pictures are examples for pylones I like

Target Market(s)

the passing cars often miss my entry...I want to show where to turn left

Colors
3276b5
33a6d7
00a990

Requirements
Must have
• High value, simple elegance, size: 250cm (high) x 100cm (width)
Nice to have
• Our Logo, arrow(?)

A special Text is not necessary but this will be an option:

Biegen sie hier ab und wir biegen es wieder hin!
Should not have
• Too much Color, the colors I have chosen are the possible colors but it‘s not necessary to use them.

```html
<!DOCTYPE html>
<html lang="de">
<head>
<meta charset="utf-8">
<title>Fernhollow Tierpraxis – Pylon</title>
<link href="https://fonts.googleapis.com/css2?family=Oswald:wght@500;600&family=Montserrat:wght@500;700;800&display=swap" rel="stylesheet">
<style>
  :root {
    --navy: #1a4a99;
    --sky: #2bb3dc;
    --band-top: #27a4d4;
    --band-bottom: #1a4fa0;
    --white: #ffffff;
    --page: #e4e4e4;
    --photo-light: #eef0f1;
    --photo-mid: #d9dcdc;
    --photo-warm: #e9dcc4;
  }
  * { box-sizing: border-box; margin: 0; padding: 0; }
  html, body { width: 1200px; height: 1028px; overflow: hidden; }
  body {
    background: var(--page);
    display: flex;
    align-items: center;
    justify-content: center;
  }
  .pylon {
    position: relative;
    width: 400px;
    height: 998px;
    overflow: hidden;
    background: var(--white);
  }
  .pylon__photo {
    position: absolute;
    left: 0; right: 0;
    top: 290px;
    height: 490px;
    background:
      radial-gradient(ellipse at 75% 65%, var(--photo-warm) 0%, rgba(233,220,196,0) 45%),
      linear-gradient(100deg, var(--photo-mid) 0%, var(--photo-light) 45%, var(--photo-light) 100%);
  }
  .pylon__shapes {
    position: absolute;
    inset: 0;
  }
  .brand {
    position: absolute;
    top: 58px;
    left: 0; right: 0;
    display: flex;
    align-items: center;
    justify-content: center;
    gap: 14px;
  }
  .brand__dot {
    width: 64px; height: 64px;
    border-radius: 50%;
    background: var(--navy);
  }
  .brand__name {
    font-family: "Oswald", sans-serif;
    font-weight: 600;
    color: var(--navy);
    line-height: 1;
    letter-spacing: 1px;
  }
  .brand__name span { display: block; }
  .brand__name .brand__main { font-size: 40px; }
  .brand__name .brand__sub { font-size: 18px; letter-spacing: 6.2px; margin-top: 4px; }
  .headline {
    position: absolute;
    top: 172px;
    left: 0; right: 0;
    text-align: center;
    font-family: "Oswald", sans-serif;
    font-weight: 500;
    font-size: 37px;
    line-height: 44px;
    transform: scaleX(0.86);
  }
  .headline__lead { color: var(--navy); display: block; }
  .headline__follow { color: var(--sky); display: block; }
  .cta {
    position: absolute;
    top: 786px;
    left: 0; right: 0;
    text-align: center;
    font-family: "Oswald", sans-serif;
    font-weight: 500;
    font-size: 31px;
    line-height: 42px;
    color: var(--white);
    transform: scaleX(0.86);
  }
  .phone {
    position: absolute;
    top: 876px;
    left: 43px;
    width: 302px;
    height: 54px;
    border-radius: 27px;
    background: var(--white);
    display: flex;
    align-items: center;
    justify-content: center;
    gap: 10px;
    font-family: "Montserrat", sans-serif;
    font-weight: 800;
    font-size: 26px;
    color: var(--navy);
  }
  .phone__icon { width: 32px; height: 32px; }
  .website {
    position: absolute;
    top: 942px;
    left: 0; right: 0;
    text-align: center;
    font-family: "Montserrat", sans-serif;
    font-weight: 500;
    font-size: 17px;
    color: var(--white);
  }
  .website strong { font-weight: 700; }
</style>
</head>
<body>
  <main class="pylon">
    <div class="pylon__photo" role="img" aria-label="Photo: smiling veterinarian in a white coat with stethoscope beside a golden retriever in a bright clinic"></div>

    <svg class="pylon__shapes" width="400" height="998" viewBox="0 0 400 998" aria-hidden="true">
      <defs>
        <linearGradient id="bandGradient" x1="0" y1="0" x2="0" y2="1">
          <stop offset="0" stop-color="#27a4d4"/>
          <stop offset="1" stop-color="#1a4fa0"/>
        </linearGradient>
        <g id="chevronRow">
          <polygon points="0,0 12,0 26,17 12,34 0,34 14,17" fill="#2bb3dc"/>
          <polygon points="20,0 32,0 46,17 32,34 20,34 34,17" fill="#1a4a99"/>
          <polygon points="40,0 52,0 66,17 52,34 40,34 54,17" fill="#2bb3dc"/>
          <polygon points="60,0 72,0 86,17 72,34 60,34 74,17" fill="#1a4a99"/>
          <polygon points="80,0 88,0 100,17 88,34 80,34 92,17" fill="#2bb3dc"/>
        </g>
      </defs>
      <polygon class="pylon__header" points="0,0 400,0 400,305 200,372 0,305" fill="#ffffff"/>
      <polygon class="pylon__band" points="0,695 200,763 400,695 400,998 0,998" fill="url(#bandGradient)"/>
      <use href="#chevronRow" x="86" y="272"/>
      <use href="#chevronRow" x="218" y="272"/>
    </svg>

    <div class="brand">
      <div class="brand__dot"></div>
      <div class="brand__name">
        <span class="brand__main">FERNHOLLOW</span>
        <span class="brand__sub">TIERPRAXIS</span>
      </div>
    </div>

    <h1 class="headline">
      <span class="headline__lead">BIEGEN SIE EIN,</span>
      <span class="headline__follow">DANN BIEGEN WIR ES HIN!</span>
    </h1>

    <p class="cta">VEREINBAREN SIE<br>GLEICH EINEN TERMIN!</p>

    <div class="phone">
      <svg class="phone__icon" viewBox="0 0 32 32" aria-hidden="true">
        <circle cx="16" cy="16" r="16" fill="#2bb3dc"/>
        <path d="M11.5 8.5c.6-.4 1.4-.3 1.8.3l1.6 2.4c.4.6.3 1.3-.2 1.8l-1 .9c.8 1.8 2.3 3.3 4.1 4.1l.9-1c.5-.5 1.2-.6 1.8-.2l2.4 1.6c.6.4.7 1.2.3 1.8l-.9 1.3c-.6.8-1.6 1.2-2.6 1-4.7-1-8.4-4.7-9.4-9.4-.2-1 .2-2 1-2.6z" fill="#ffffff"/>
      </svg>
      <span class="phone__number">+43 3155 48210</span>
    </div>

    <p class="website">www.<strong>fernhollow-tierpraxis</strong>.at</p>
  </main>
</body>
</html>
```